Cutting Edge Cloud Hosting Provider needs business card design

We are a new Cloud Hosting Provider called Velkaro Hosting. (Velkaro means cloudy in Spanish.) We provide clients with virtual resources and not virtual machines directly. Our clients purchase the resources that they will use (RAM,CPU, Hard drive space) then use those resources in as many virtual machines as they like.

We are looking for a business card design that is cutting edge and hip.
Updates

The name of the company is "Velkaro Hosting". Please include the "Hosting" part of our name in the design.

Thanks

Target Market(s)

21-35 developers and I.T. Staff

Industry/Entity Type

Business

Requirements
Must have
• Rounded corners, Must Incorporate our logo, individual's name must be prominent

```html
<!DOCTYPE html>
<html lang="en">
<head>
<meta charset="utf-8">
<title>Velkaro Hosting — Business Card</title>
<link rel="stylesheet" href="https://fonts.googleapis.com/css2?family=Syncopate:wght@400;700&display=swap">
<style>
  :root {
    --backdrop: #e8e4dc;
    --card-light: #ffffff;
    --card-mid: #dde2e1;
    --card-edge: #c3cbc9;
    --navy: #1d2c80;
    --ink: #1a1a1a;
    --teal-dark: #1f3a40;
    --teal: #4b8c93;
  }
  html, body {
    margin: 0;
    padding: 0;
    width: 1200px;
    height: 900px;
    overflow: hidden;
    background: var(--backdrop);
    font-family: "Syncopate", sans-serif;
  }
  .canvas {
    position: relative;
    width: 1200px;
    height: 900px;
  }
  .card {
    position: absolute;
    width: 585px;
    height: 365px;
    border-radius: 14px;
    overflow: hidden;
    box-shadow: 0 2px 6px rgba(0,0,0,0.18);
  }
  .card--front {
    left: 72px;
    top: 60px;
    background: radial-gradient(ellipse 320px 220px at 200px 230px, var(--card-light) 0%, var(--card-mid) 55%, var(--card-edge) 100%);
  }
  .card--back {
    left: 545px;
    top: 466px;
    background: radial-gradient(ellipse 340px 230px at 200px 270px, var(--card-light) 0%, var(--card-mid) 55%, var(--card-edge) 100%);
  }
  .brand-name {
    position: absolute;
    margin: 0;
    color: var(--navy);
    font-weight: 400;
    letter-spacing: 1px;
  }
  .card--front .brand-name {
    left: 54px;
    top: 62px;
    font-size: 34px;
  }
  .card--back .brand-name {
    left: 0;
    right: 0;
    top: 160px;
    text-align: center;
    font-size: 44px;
  }
  .person {
    position: absolute;
    left: 40px;
    top: 188px;
    width: 210px;
    text-align: center;
  }
  .person__name {
    margin: 0;
    color: var(--navy);
    font-size: 19px;
    font-weight: 400;
    letter-spacing: 1.5px;
  }
  .person__title {
    margin: 6px 0 0;
    color: var(--ink);
    font-size: 10px;
    letter-spacing: 0.5px;
  }
  .divider {
    position: absolute;
    left: 266px;
    top: 185px;
    width: 3px;
    height: 88px;
    background: linear-gradient(to bottom, rgba(75,140,147,0), var(--teal) 40%, var(--teal-dark) 70%, rgba(31,58,64,0));
  }
  .company {
    position: absolute;
    left: 304px;
    top: 154px;
    margin: 0;
    font-style: normal;
    color: var(--ink);
    font-size: 12px;
    line-height: 16px;
    letter-spacing: 1.5px;
  }
  .company__name {
    display: block;
    color: var(--navy);
    font-size: 15px;
    letter-spacing: 2px;
    margin-bottom: 2px;
  }
  .contact {
    position: absolute;
    left: 300px;
    top: 245px;
    margin: 0;
    font-style: normal;
    color: var(--ink);
    font-size: 12px;
    line-height: 19px;
    letter-spacing: 1.5px;
  }
  .band {
    position: absolute;
    left: 0;
    bottom: 0;
    width: 100%;
    height: 20px;
  }
  .rule {
    position: absolute;
    left: 102px;
    top: 234px;
    width: 380px;
    height: 4px;
    border-radius: 2px;
    background: linear-gradient(to right, rgba(31,58,64,0.1), var(--teal-dark) 30%, var(--teal) 70%, rgba(75,140,147,0.1));
  }
  .tagline {
    position: absolute;
    left: 0;
    right: 0;
    top: 252px;
    margin: 0;
    text-align: center;
    color: var(--ink);
    font-size: 13px;
    line-height: 20px;
    letter-spacing: 1.5px;
    font-weight: 700;
  }
</style>
</head>
<body>
<main class="canvas">
  <section class="card card--front" aria-label="Business card front">
    <p class="brand-name">velkaro</p>
    <div class="person">
      <h1 class="person__name">Marco Ledesma</h1>
      <p class="person__title">Vice-President</p>
    </div>
    <div class="divider"></div>
    <address class="company">
      <span class="company__name">Velkaro Hosting</span>
      417 Alder Row<br>
      Corvale, TX 78100
    </address>
    <address class="contact">
      p. 555.014.2280<br>
      c. 555.019.4432<br>
      marco@velkaro.com
    </address>
    <svg class="band" viewBox="0 0 585 20" preserveAspectRatio="none" aria-hidden="true">
      <defs>
        <linearGradient id="bandFill" x1="0" x2="1" y1="0" y2="0">
          <stop offset="0" stop-color="#1f3a40"/>
          <stop offset="0.55" stop-color="#4b8c93"/>
          <stop offset="1" stop-color="#2a4f55"/>
        </linearGradient>
      </defs>
      <rect x="0" y="0" width="585" height="20" fill="url(#bandFill)"/>
      <circle cx="556" cy="0" r="13" fill="#dde2e1"/>
    </svg>
  </section>

  <section class="card card--back" aria-label="Business card back">
    <p class="brand-name">velkaro</p>
    <div class="rule"></div>
    <p class="tagline">Infrastructure as a Service<br>Platform as a Service | Automation</p>
  </section>
</main>
</body>
</html>
```